Kestrelbay Racquet Club app

Design a sporting app that can, post news, post events, capture and show live scores, link at least 6 websites, other functions would be an advantage. Real tennis is also known as Royal tennis and Court tennis.
This would be like a sporting clubs app that gives live scores.

Colors

Designer to choose colors to be used in the design.

Requirements
Must have
• post news, post events, capture and show live scores, link at least 6 websites,
Nice to have
• Instructions on how to launch the app on apple and android

```html
<!DOCTYPE html>
<html lang="en">
<head>
<meta charset="utf-8">
<title>Kestrelbay Racquet Club app</title>
<link href="https://fonts.googleapis.com/css2?family=Montserrat:wght@400;500;600;700&display=swap" rel="stylesheet">
<style>
:root{
  --stage:#bdbdbd;
  --navy:#0e0a7c;
  --blue:#1f4df2;
  --lavender:#8e9cf6;
  --red:#f0483e;
  --ink:#1e1e2a;
  --muted:#8a8a96;
  --line:#ececf2;
  --card:#ffffff;
  --photo-skin:#c9a28a;
  --photo-court:#1c4fb8;
}
*{box-sizing:border-box;margin:0;padding:0}
html,body{width:1026px;height:1200px;overflow:hidden}
body{background:var(--stage);font-family:"Montserrat",sans-serif;color:var(--ink);position:relative}
.screen{position:absolute;width:200px;height:434px;background:#fff;border-radius:16px;overflow:hidden}
.abs{position:absolute}
.brand{position:absolute;left:10px;top:24px;font-size:6px;font-weight:700;color:var(--navy)}
.title{position:absolute;top:22px;left:0;right:0;text-align:center;font-size:9px;font-weight:600}
.alert{position:absolute;right:10px;top:21px}
.tabs{position:absolute;top:56px;left:10px;right:10px;display:flex;justify-content:space-between;font-size:7.5px;font-weight:500}
.tabs .on{border-bottom:1.5px solid var(--blue);padding-bottom:3px}
.tabbar-shadow{position:absolute;left:0;right:0;top:72px;height:8px;background:linear-gradient(#f2f2f6,#fff)}
.score-card{position:absolute;left:8px;right:8px;height:76px;background:var(--card);border-radius:6px;box-shadow:0 2px 8px rgba(20,20,60,.08)}
.pill{position:absolute;top:-8px;left:50%;transform:translateX(-50%);background:var(--blue);color:#fff;font-size:7.5px;font-weight:600;padding:3px 14px;border-radius:9px;white-space:nowrap}
.court{position:absolute;left:7px;top:10px;font-size:7px;color:#555}
.clock{position:absolute;right:8px;top:10px;font-size:7.5px;color:#555}
.row{position:absolute;left:7px;right:8px;height:20px;display:flex;align-items:center;font-size:6.5px}
.avatar{width:16px;height:20px;border-radius:2px;background:linear-gradient(#d9b59c,#6c7fb8)}
.flag{width:11px;height:7px;margin-left:6px;border-radius:1px}
.pname{margin-left:5px;font-weight:600;width:46px}
.sets{color:var(--muted);width:10px}
.pts{margin-left:auto;display:flex;gap:6px;align-items:center}
.pts b{font-weight:700}
.pts span{color:var(--muted)}
.serve{width:6px;height:6px;border-radius:50%;border:1.5px solid var(--navy)}
.nav{position:absolute;left:0;right:0;bottom:0;height:43px;background:var(--navy);display:flex;justify-content:space-around;align-items:center;padding:0 6px}
.nav svg{width:12px;height:12px}
.hub{position:absolute;left:50%;top:-22px;transform:translateX(-50%);width:42px;height:42px;border-radius:50%;background:#fff;display:flex;align-items:center;justify-content:center}
.hub i{width:26px;height:26px;border-radius:50%;background:var(--navy);display:flex;align-items:center;justify-content:center}
.spacer{width:24px}
.date{position:absolute;left:9px;top:52px;font-size:11px;font-weight:600;color:#8d8d98;line-height:14px}
.btn{position:absolute;right:9px;top:57px;background:var(--navy);color:#fff;font-size:8px;font-weight:600;padding:8px 9px;border-radius:5px}
.section{position:absolute;left:9px;font-size:11px;font-weight:700;display:flex;align-items:center;gap:5px}
.section::after{content:"";width:26px;height:1.2px;background:var(--blue)}
.event-card{position:absolute;width:80px;height:106px;background:#fff;border-radius:5px;box-shadow:0 2px 8px rgba(20,20,60,.09);overflow:hidden;font-size:5px}
.event-card::before{content:"";position:absolute;left:0;right:0;top:0;height:5px;background:var(--lavender)}
.match{position:absolute;top:14px;left:0;right:0;display:flex;justify-content:space-around;align-items:center}
.match .avatar{width:13px;height:17px}
.match b{font-size:8px;font-weight:700}
.names{position:absolute;top:34px;left:3px;right:3px;display:flex;justify-content:space-between;color:#444}
.meta{position:absolute;left:8px;display:flex;align-items:center;gap:5px;color:#444}
.badge{position:absolute;bottom:8px;left:50%;transform:translateX(-50%);width:16px;height:16px;border-radius:50%;background:#d7d9ea}
.hero-top{position:absolute;left:0;right:0;top:0;height:60px;background:linear-gradient(90deg,#f3f3f8,#ffffff 40%,#e9e8f8 70%,#c9c3f0)}
.indicator{position:absolute;left:93px;top:57px;width:14px;height:1.6px;background:var(--navy)}
.strip{position:absolute;left:0;right:0;top:63px;height:5px;background:var(--lavender)}
.portrait{position:absolute;top:78px;width:36px;height:64px;border-radius:2px;background:linear-gradient(#c9a28a,#2d5dc7)}
.center-text{position:absolute;left:0;right:0;text-align:center;font-size:8px}
.center-text.bold{font-weight:700}
.hero-photo{position:absolute;left:0;right:0;bottom:0;height:118px;background:linear-gradient(90deg,#d8cfc8,#f0ece9 50%,#cbb4a4)}
.camera-photo{position:absolute;inset:0;background:linear-gradient(160deg,#2a62cf,#184aa8 55%,#143d90)}
.shutter{position:absolute;left:83px;top:321px;width:37px;height:37px;border-radius:50%;border:4px solid var(--red);background:#262626}
.post-box{position:absolute;left:8px;right:8px;top:56px;height:43px;background:#fff;border-radius:6px;box-shadow:0 2px 8px rgba(20,20,60,.08);display:flex;align-items:center;padding:0 8px;gap:8px;font-size:6.5px;color:#b4b4bd}
.me{width:27px;height:27px;border-radius:50%;background:linear-gradient(#a7a087,#5e6a5c)}
.news{position:absolute;left:8px;right:8px;height:50px;background:#fff;border-radius:5px;box-shadow:0 2px 8px rgba(20,20,60,.08)}
.news .who{position:absolute;left:8px;top:9px;display:flex;align-items:center;gap:5px;font-size:7.5px;font-weight:600}
.news .who i{width:11px;height:11px;border-radius:50%;background:linear-gradient(#c9a28a,#6d5b52)}
.news p{position:absolute;left:8px;top:25px;width:100px;font-size:6px;line-height:8px;color:#444}
.thumb{position:absolute;right:8px;top:8px;width:48px;height:33px;border-radius:2px;background:linear-gradient(#4f7552,#7fa36b)}
</style>
</head>
<body>

<!-- Scores -->
<section class="screen" style="left:95px;top:112px">
  <span class="brand">Kestrelbay</span>
  <h1 class="title">Scores</h1>
  <svg class="alert" width="11" height="11" viewBox="0 0 11 11"><rect x="1" y="2" width="8" height="8" fill="none" stroke="#f0483e" stroke-width="1.2"/><circle cx="9" cy="2" r="1.8" fill="#f0483e"/></svg>
  <nav class="tabs"><span class="on">Live</span><span>Schedule</span><span>Completed</span><span>Draws</span></nav>
  <div class="tabbar-shadow"></div>

  <article class="score-card" style="top:109px">
    <span class="pill">Semi-Final</span><span class="court">Court 1</span><span class="clock">1:45:40</span>
    <div class="row" style="top:23px"><i class="avatar" role="img" aria-label="Player portrait"></i><i class="flag" style="background:#e0282e"></i><span class="pname">R. Falkner</span><span class="sets">4</span><span class="pts"><i class="serve"></i><b>30</b><span>6</span><span>2</span><span>6</span></span></div>
    <div class="row" style="top:48px"><i class="avatar" role="img" aria-label="Player portrait"></i><i class="flag" style="background:linear-gradient(#c8102e 25%,#f2c200 25% 75%,#c8102e 75%)"></i><span class="pname">R. Navarro</span><span class="sets">5</span><span class="pts"><b>15</b><span>3</span><span>6</span><span>5</span></span></div>
  </article>

  <article class="score-card" style="top:206px">
    <span class="pill">Round 2</span><span class="court">Court 2</span><span class="clock">00:20:20</span>
    <div class="row" style="top:23px"><i class="avatar" role="img" aria-label="Player portrait"></i><i class="flag" style="background:repeating-linear-gradient(#b22234 0 1px,#fff 1px 2px)"></i><span class="pname">S. Whitley</span><span class="sets">1</span><span class="pts"><i class="serve"></i><b>30</b></span></div>
    <div class="row" style="top:48px"><i class="avatar" role="img" aria-label="Player portrait"></i><i class="flag" style="background:#1e3a8a"></i><span class="pname">A. Bartram</span><span class="sets">2</span><span class="pts"><b>15</b></span></div>
  </article>

  <article class="score-card" style="top:300px">
    <span class="pill">Quarters</span><span class="court">Court 1</span><span class="clock">00:45:40</span>
    <div class="row" style="top:23px"><i class="avatar" role="img" aria-label="Player portrait"></i><i class="flag" style="background:linear-gradient(#c6363c 33%,#0c4076 33% 66%,#fff 66%)"></i><span class="pname">N. Dragovic</span><span class="sets">2</span><span class="pts"><i class="serve"></i><b>30</b><span>6</span></span></div>
    <div class="row" style="top:48px"><i class="avatar" role="img" aria-label="Player portrait"></i><i class="flag" style="background:linear-gradient(#000 33%,#dd0000 33% 66%,#ffce00 66%)"></i><span class="pname">A. Zorin</span><span class="sets">3</span><span class="pts"><b>15</b><span>5</span></span></div>
  </article>

  <nav class="nav">
    <svg viewBox="0 0 12 12"><circle cx="7.5" cy="4.5" r="3.5" fill="none" stroke="#8e9cf6" stroke-width="1.2"/><path d="M5 7 1 11" stroke="#8e9cf6" stroke-width="1.4"/></svg>
    <svg viewBox="0 0 12 12"><rect x="1" y="2" width="10" height="9" fill="none" stroke="#8e9cf6" stroke-width="1.2"/><path d="M1 5h10M4 0v3M8 0v3" stroke="#8e9cf6"/></svg>
    <span class="spacer"></span>
    <svg viewBox="0 0 12 12"><rect x="1.5" y="1" width="9" height="10" fill="none" stroke="#8e9cf6" stroke-width="1.2"/><path d="M3.5 4h5M3.5 6h5M3.5 8h3" stroke="#8e9cf6"/></svg>
    <svg viewBox="0 0 12 12"><circle cx="6" cy="4" r="2.5" fill="none" stroke="#8e9cf6" stroke-width="1.2"/><path d="M1.5 11.5c0-3 2-4.5 4.5-4.5s4.5 1.5 4.5 4.5" fill="none" stroke="#8e9cf6" stroke-width="1.2"/></svg>
    <span class="hub"><i><svg viewBox="0 0 12 12"><circle cx="6" cy="6" r="4.5" fill="none" stroke="#fff" stroke-width="1.2"/><circle cx="6" cy="6" r="1.6" fill="#fff"/></svg></i></span>
  </nav>
</section>

<!-- Events -->
<section class="screen" style="left:414px;top:112px">
  <span class="brand">Kestrelbay</span>
  <h1 class="title">Events</h1>
  <svg class="alert" width="11" height="11" viewBox="0 0 11 11"><rect x="1" y="2" width="8" height="8" fill="none" stroke="#f0483e" stroke-width="1.2"/><circle cx="9" cy="2" r="1.8" fill="#f0483e"/></svg>
  <p class="date">Thursday<br>24 Dec</p>
  <span class="btn">Add Events</span>

  <h2 class="section" style="top:113px">Popular</h2>
  <article class="event-card" style="left:9px;top:136px">
    <div class="match"><i class="avatar" role="img" aria-label="Player portrait"></i><b>VS</b><i class="avatar" role="img" aria-label="Player portrait"></i></div>
    <div class="names"><span>R. Falkner</span><span>R. Navarro</span></div>
    <div class="meta" style="top:48px"><svg width="7" height="7" viewBox="0 0 7 7"><rect x=".5" y="1" width="6" height="5.5" fill="none" stroke="#1f4df2" stroke-width=".8"/></svg>12-24-2019</div>
    <div class="meta" style="top:61px"><svg width="7" height="6" viewBox="0 0 7 6"><ellipse cx="3.5" cy="3" rx="3" ry="2.3" fill="none" stroke="#1f4df2" stroke-width=".8"/></svg>Brisbane</div>
    <span class="badge"></span>
  </article>
  <article class="event-card" style="left:98px;top:136px">
    <div class="match"><i class="avatar" role="img" aria-label="Player portrait"></i><b>VS</b><i class="avatar" role="img" aria-label="Player portrait"></i></div>
    <div class="names"><span>S. Whitley</span><span>A. Bartram</span></div>
    <div class="meta" style="top:48px"><svg width="7" height="7" viewBox="0 0 7 7"><rect x=".5" y="1" width="6" height="5.5" fill="none" stroke="#1f4df2" stroke-width=".8"/></svg>12-24-2019</div>
    <div class="meta" style="top:61px"><svg width="7" height="6" viewBox="0 0 7 6"><ellipse cx="3.5" cy="3" rx="3" ry="2.3" fill="none" stroke="#1f4df2" stroke-width=".8"/></svg>London</div>
    <span class="badge"></span>
  </article>
  <article class="event-card" style="left:187px;top:136px"></article>

  <h2 class="section" style="top:256px">Trending</h2>
  <article class="event-card" style="left:9px;top:279px">
    <div class="match"><i class="avatar" role="img" aria-label="Player portrait"></i><b>VS</b><i class="avatar" role="img" aria-label="Player portrait"></i></div>
    <div class="names"><span>M. Ravel</span><span>D. Medvin</span></div>
    <div class="meta" style="top:48px"><svg width="7" height="7" viewBox="0 0 7 7"><rect x=".5" y="1" width="6" height="5.5" fill="none" stroke="#1f4df2" stroke-width=".8"/></svg>12-24-2019</div>
    <div class="meta" style="top:61px"><svg width="7" height="6" viewBox="0 0 7 6"><ellipse cx="3.5" cy="3" rx="3" ry="2.3" fill="none" stroke="#1f4df2" stroke-width=".8"/></svg>Belgium</div>
    <span class="badge"></span>
  </article>
  <article class="event-card" style="left:98px;top:279px">
    <div class="match"><i class="avatar" role="img" aria-label="Player portrait"></i><b>VS</b><i class="avatar" role="img" aria-label="Player portrait"></i></div>
    <div class="names"><span>A. Zorin</span><span>D. Dragovic</span></div>
    <div class="meta" style="top:48px"><svg width="7" height="7" viewBox="0 0 7 7"><rect x=".5" y="1" width="6" height="5.5" fill="none" stroke="#1f4df2" stroke-width=".8"/></svg>12-24-2019</div>
    <div class="meta" style="top:61px"><svg width="7" height="6" viewBox="0 0 7 6"><ellipse cx="3.5" cy="3" rx="3" ry="2.3" fill="none" stroke="#1f4df2" stroke-width=".8"/></svg>New York</div>
    <span class="badge"></span>
  </article>
  <article class="event-card" style="left:187px;top:279px"></article>

  <nav class="nav">
    <svg viewBox="0 0 12 12"><circle cx="7.5" cy="4.5" r="3.5" fill="none" stroke="#8e9cf6" stroke-width="1.2"/><path d="M5 7 1 11" stroke="#8e9cf6" stroke-width="1.4"/></svg>
    <svg viewBox="0 0 12 12"><rect x="1" y="2" width="10" height="9" fill="none" stroke="#fff" stroke-width="1.2"/><path d="M1 5h10M4 0v3M8 0v3" stroke="#fff"/></svg>
    <span class="spacer"></span>
    <svg viewBox="0 0 12 12"><rect x="1.5" y="1" width="9" height="10" fill="none" stroke="#8e9cf6" stroke-width="1.2"/><path d="M3.5 4h5M3.5 6h5M3.5 8h3" stroke="#8e9cf6"/></svg>
    <svg viewBox="0 0 12 12"><circle cx="6" cy="4" r="2.5" fill="none" stroke="#8e9cf6" stroke-width="1.2"/><path d="M1.5 11.5c0-3 2-4.5 4.5-4.5s4.5 1.5 4.5 4.5" fill="none" stroke="#8e9cf6" stroke-width="1.2"/></svg>
    <span class="hub"><i><svg viewBox="0 0 12 12"><circle cx="6" cy="6" r="4.5" fill="none" stroke="#fff" stroke-width="1.2"/><circle cx="6" cy="6" r="1.6" fill="#fff"/></svg></i></span>
  </nav>
</section>

<!-- Match detail -->
<section class="screen" style="left:731px;top:112px">
  <div class="hero-top" role="img" aria-label="Blurred arena photo"></div>
  <span class="indicator"></span>
  <span class="strip"></span>
  <i class="portrait" style="left:24px" role="img" aria-label="Player portrait"></i>
  <span class="abs" style="left:93px;top:105px;font-size:8px;font-weight:600">VS</span>
  <i class="portrait" style="left:120px" role="img" aria-label="Player portrait"></i>
  <span class="abs" style="left:22px;top:150px;font-size:8px;font-weight:600">R. Falkner</span>
  <span class="abs" style="left:121px;top:150px;font-size:8px;font-weight:600">R. Navarro</span>
  <svg class="abs" style="left:95px;top:166px" width="10" height="10" viewBox="0 0 10 10"><rect x="1" y="2" width="8" height="7" fill="none" stroke="#1f4df2" stroke-width="1"/><path d="M1 4.5h8" stroke="#1f4df2"/></svg>
  <p class="center-text" style="top:180px">12-24-2019</p>
  <svg class="abs" style="left:94px;top:200px" width="12" height="8" viewBox="0 0 12 8"><ellipse cx="6" cy="4" rx="5" ry="3" fill="none" stroke="#1f4df2" stroke-width="1"/></svg>
  <p class="center-text" style="top:220px">Harbourside Arena</p>
  <p class="center-text bold" style="top:243px">Gates Open</p>
  <p class="center-text" style="top:261px">10:00 am</p>
  <p class="center-text bold" style="top:279px">Session</p>
  <p class="center-text" style="top:297px">Day</p>
  <div class="hero-photo" role="img" aria-label="Photo of the two finalists"></div>
</section>

<!-- Capture -->
<section class="screen" style="left:253px;top:654px">
  <div class="camera-photo" role="img" aria-label="Photo of a player hitting a backhand on a blue court"></div>
  <svg class="abs" style="left:11px;top:24px" width="11" height="11" viewBox="0 0 11 11"><circle cx="5.5" cy="5.5" r="3.8" fill="none" stroke="#fff" stroke-width="1.3" stroke-dasharray="2 1"/><circle cx="5.5" cy="5.5" r="1.4" fill="#fff"/></svg>
  <svg class="abs" style="left:180px;top:23px" width="8" height="12" viewBox="0 0 8 12"><path d="M5 0 1 7h3l-1 5 4-7H4z" fill="#fff"/></svg>
  <span class="shutter"></span>
  <svg class="abs" style="left:167px;top:334px" width="12" height="10" viewBox="0 0 12 10"><rect x="1" y="2" width="10" height="7" rx="1" fill="none" stroke="#fff" stroke-width="1"/><circle cx="6" cy="5.5" r="2" fill="none" stroke="#fff"/></svg>
  <nav class="nav">
    <svg viewBox="0 0 12 12"><path d="M3 1h6v3a3 3 0 0 1-6 0zM6 7v3M3.5 11h5" fill="none" stroke="#8e9cf6" stroke-width="1.2"/></svg>
    <svg viewBox="0 0 12 12"><rect x="1" y="2" width="10" height="9" fill="none" stroke="#8e9cf6" stroke-width="1.2"/><path d="M1 5h10M4 0v3M8 0v3" stroke="#8e9cf6"/></svg>
    <span class="spacer"></span>
    <svg viewBox="0 0 12 12"><rect x="1.5" y="1" width="9" height="10" fill="none" stroke="#8e9cf6" stroke-width="1.2"/><path d="M3.5 4h5M3.5 6h5M3.5 8h3" stroke="#8e9cf6"/></svg>
    <svg viewBox="0 0 12 12"><circle cx="6" cy="4" r="2.5" fill="none" stroke="#8e9cf6" stroke-width="1.2"/><path d="M1.5 11.5c0-3 2-4.5 4.5-4.5s4.5 1.5 4.5 4.5" fill="none" stroke="#8e9cf6" stroke-width="1.2"/></svg>
    <span class="hub" style="background:#2b4fb0"><i><svg viewBox="0 0 12 12"><circle cx="6" cy="6" r="4.5" fill="none" stroke="#fff" stroke-width="1.2"/><circle cx="6" cy="6" r="1.6" fill="#fff"/></svg></i></span>
  </nav>
</section>

<!-- News -->
<section class="screen" style="left:572px;top:654px">
  <span class="brand">Kestrelbay</span>
  <h1 class="title">News</h1>
  <svg class="alert" width="11" height="11" viewBox="0 0 11 11"><rect x="1" y="2" width="8" height="8" fill="none" stroke="#f0483e" stroke-width="1.2"/><circle cx="9" cy="2" r="1.8" fill="#f0483e"/></svg>
  <div class="post-box"><i class="me" role="img" aria-label="Member avatar"></i><span>What's the great news</span><svg style="margin-left:auto" width="11" height="10" viewBox="0 0 11 10"><rect x="1" y="1.5" width="9" height="7.5" fill="none" stroke="#1f4df2" stroke-width="1"/><path d="M3 6.5l2-2 3 3" fill="none" stroke="#1f4df2"/></svg></div>
  <h2 class="abs" style="left:9px;top:118px;font-size:11px;font-weight:700">Latest News</h2>

  <article class="news" style="top:148px"><span class="who"><i></i>Amanda Hollis</span><p>Dragovic to face Navarro in the finals can't wait for the battle to start.</p><span class="thumb" role="img" aria-label="Photo of a stadium court"></span></article>
  <article class="news" style="top:204px"><span class="who"><i></i>Carol Esteban</span><p>Falkner continues his winning streak.</p><span class="thumb" role="img" aria-label="Photo of a player on grass"></span></article>
  <article class="news" style="top:260px"><span class="who"><i></i>Kathy Wells</span><p>I'm starting to coach U-19 girls from 1st January.</p><span class="thumb" style="background:linear-gradient(#3a3f4a,#6b707a)" role="img" aria-label="Photo gallery of a coaching session"><span style="position:absolute;left:18px;top:11px;color:#fff;font-size:8px">+5</span></span></article>
  <article class="news" style="top:316px"><span class="who"><i></i>Walter Schindler</span><p>Shalimova wins the 3rd title in a row this year.</p><span class="thumb" role="img" aria-label="Photo of a player celebrating"></span></article>

  <nav class="nav">
    <svg viewBox="0 0 12 12"><circle cx="7.5" cy="4.5" r="3.5" fill="none" stroke="#8e9cf6" stroke-width="1.2"/><path d="M5 7 1 11" stroke="#8e9cf6" stroke-width="1.4"/></svg>
    <svg viewBox="0 0 12 12"><rect x="1" y="2" width="10" height="9" fill="none" stroke="#8e9cf6" stroke-width="1.2"/><path d="M1 5h10M4 0v3M8 0v3" stroke="#8e9cf6"/></svg>
    <span class="spacer"></span>
    <svg viewBox="0 0 12 12"><rect x="1.5" y="1" width="9" height="10" fill="none" stroke="#fff" stroke-width="1.2"/><path d="M3.5 4h5M3.5 6h5M3.5 8h3" stroke="#fff"/></svg>
    <svg viewBox="0 0 12 12"><circle cx="6" cy="4" r="2.5" fill="none" stroke="#8e9cf6" stroke-width="1.2"/><path d="M1.5 11.5c0-3 2-4.5 4.5-4.5s4.5 1.5 4.5 4.5" fill="none" stroke="#8e9cf6" stroke-width="1.2"/></svg>
    <span class="hub"><i><svg viewBox="0 0 12 12"><circle cx="6" cy="6" r="4.5" fill="none" stroke="#fff" stroke-width="1.2"/><circle cx="6" cy="6" r="1.6" fill="#fff"/></svg></i></span>
  </nav>
</section>

</body>
</html>
```